Business Card and Stationary for Electrical Contractor
Vantor Electric
Business Card and Stationary for Electrical Contractor - Construction
Creative Brief
Professional
Dalton Pryce
Service Technician
1875 Birchwood Lane Kansas City, KS 66109
dpryce@vantorelectricmo.com
www.vantorelectricmo.com

```html
<!DOCTYPE html>
<html lang="en">
<head>
<meta charset="utf-8">
<title>Vantor Electric – Business Card</title>
<link rel="stylesheet" href="https://fonts.googleapis.com/css2?family=Montserrat:wght@400;600;700&display=swap">
<style>
  :root {
    --backdrop: #3b3b3d;
    --card: #141414;
    --card-edge: #d3222a;
    --accent: #d3222a;
    --ink: #ffffff;
    --ink-soft: #c9c9c9;
    --emboss: #6a6a6a;
  }
  * { margin: 0; padding: 0; box-sizing: border-box; }
  html, body {
    width: 1200px; height: 840px; overflow: hidden;
    background: var(--backdrop);
    font-family: "Montserrat", sans-serif;
  }
  .stage {
    position: relative; width: 1200px; height: 840px;
    display: flex; align-items: center; justify-content: center; gap: 40px;
  }
  .card {
    position: relative; width: 540px; height: 309px;
    background: var(--card);
    border-bottom: 3px solid var(--card-edge);
    border-right: 3px solid var(--card-edge);
    border-radius: 2px;
  }
  /* Details side */
  .card-details .brand {
    position: absolute; left: 40px; bottom: 62px;
    display: flex; align-items: center; gap: 12px;
  }
  .brand-square { width: 22px; height: 22px; background: var(--accent); }
  .brand-name {
    color: var(--ink); font-weight: 600; font-size: 22px;
    letter-spacing: 1px; text-transform: uppercase;
  }
  .divider {
    position: absolute; left: 250px; top: 42px; width: 1px; height: 150px;
    background: var(--accent);
  }
  .contact {
    position: absolute; left: 272px; top: 40px; color: var(--ink-soft);
    font-size: 11px; line-height: 1.5;
  }
  .contact .person {
    color: var(--ink); font-weight: 700; font-size: 16px;
    letter-spacing: 1.5px; text-transform: uppercase; line-height: 1.2;
  }
  .contact .role { font-size: 11px; margin-bottom: 12px; }
  .contact .address { margin-bottom: 12px; }
  .contact ul { list-style: none; }
  .contact li { display: flex; align-items: center; gap: 8px; }
  .contact svg { width: 10px; height: 10px; fill: var(--accent); flex: none; }
  /* Logo side */
  .card-logo { display: flex; align-items: center; justify-content: center; }
  .card-logo .brand-name {
    color: var(--emboss); font-size: 44px; letter-spacing: 4px;
  }
</style>
</head>
<body>
<main class="stage">
  <section class="card card-details">
    <div class="brand">
      <span class="brand-square"></span>
      <span class="brand-name">Vantor Electric</span>
    </div>
    <div class="divider"></div>
    <div class="contact">
      <p class="person">Dalton Pryce</p>
      <p class="role">Service Technician</p>
      <p class="address">1875 Birchwood Lane<br>Kansas City, KS 66109</p>
      <ul>
        <li><svg viewBox="0 0 10 10"><path d="M2 0h2l1 3-1.5 1a6 6 0 0 0 2.5 2.5L7 5l3 1v2a2 2 0 0 1-2 2A8 8 0 0 1 0 2a2 2 0 0 1 2-2z"/></svg>913-555-0142</li>
        <li><svg viewBox="0 0 10 10"><rect x="2.5" y="0" width="5" height="10" rx="1"/></svg>816-555-0187</li>
        <li><svg viewBox="0 0 10 10"><path d="M0 2h10v6H0z M0 2l5 3.5L10 2" fill="none" stroke="#d3222a" stroke-width="1"/></svg>dpryce@vantorelectricmo.com</li>
        <li><svg viewBox="0 0 10 10"><circle cx="5" cy="5" r="4.3" fill="none" stroke="#d3222a" stroke-width="1"/><path d="M0.7 5h8.6M5 0.7v8.6" stroke="#d3222a" stroke-width="0.8"/></svg>www.vantorelectricmo.com</li>
      </ul>
    </div>
  </section>
  <section class="card card-logo">
    <span class="brand-name">Vantor Electric</span>
  </section>
</main>
</body>
</html>
```